Design für ein Flyer mit Gutschein-Abriss
Zielgruppe
Handgemachte/ handgefertigte Körperpflege- und Kosmetikprodukte, die in kleinen Chargen gefertigt werden (somit wechselnde Produkte, die in bestimmten Mengen verfügbar sind) u.a. Seifen, Rasierseifen, Badezusätze, Gesichtspflege usw.
Die Produkte werden ohne künstliche Zusätze und Konservierungsstoffe hergestellt und erhalten so wenig Allergene-Stoffe wie möglich, zum Teil vegan.
In geringem Umfang werden ebenfalls Zubehör für Körperpflege vermarktet (z.B. Lavastein für Hornhautentfernung etc.).
Die Produkte werden online und im stationären Handel vertrieben.
Ansprechen von möglichst allen Altersgruppen.
Zielgruppe: 'Otto-Normal-Verbraucher', FRAUEN, Eltern (Mutter-Kind), Männer, in geringem Umfang Haustierbesitzer (Hundeshampoos etc.)
Aufgabenstellung
Größe: DinA5
Wir führen folgende Produkte in unserer Manufaktur:
Natürliche handgefertigte Naturseifen (Milchseifen, Kräuterseifen, Aromaseifen, uvm.), Seifentorten, Seifen- und Badecupcakes, handgerollte Badetrüffel, Badesalz, Badeöle, Badeeis, Badefondant, Körper- und Gesichtspflegeprodukte, Badezubehör, Aromatherapie, Dekorationsartikel sowie Geschenkkörbe für Privat- und Firmenkunden.
Die Produkte enthalten natürliche Inhaltsstoffe, zum Teil hochwertige ätherische Öle und sind Paraben- und SLS-frei. Unsere Produkte werden nicht an Tieren getestet. Wir achten bei der Auswahl der Inhaltsstoffe und unseren Lieferanten auf fairen Handel und nachhaltige Produktion.
Des Weiteren führen wir handgemachte Sojawachskerzen, diese sind Paraffin frei und enthalten Sojawachs aus nachhaltiger Produktion.
Der Flyer soll am unteren Rand den Gutschein beinhalten, welches abgeschnitten werden kann (mit 20 % Rabatt gilt für Online und im Laden).
Auf den Flyer sollten auf jeden Fall noch folgende Daten:
Neueröffnung am 05.05.2017
www.quorvalhaus.de
Öffnungszeiten: Freitags von 11:00 bis 18:00 Uhr
Anbei unser Logo so wie ein Link mit Bildern einiger unserer Produkte.
https://www.filetrunk-beispiel.de/sh/x81kqpwe3rd7h2t/ZZZ4mNbVtRKo2LPw8cY37XUhe?dl=0
Wir freuen uns schon auf viele tolle Vorschläge.

```html
<!DOCTYPE html>
<html lang="de">
<head>
<meta charset="utf-8">
<title>Quorval Haus – Flyer Neueröffnung</title>
<link rel="stylesheet" href="https://fonts.googleapis.com/css2?family=Open+Sans:wdth,wght@75..100,300..700&display=swap">
<style>
  :root {
    --bg: #d9d9d9;
    --paper: #ffffff;
    --green: #8cab2c;
    --green-dark: #7a9624;
    --text-grey: #a3a3a3;
    --text-dark: #6f6f6f;
    --coupon-line: #ffffff;
  }
  * { box-sizing: border-box; margin: 0; padding: 0; }
  html, body {
    width: 1200px; height: 960px; overflow: hidden;
    background: var(--bg);
    font-family: "Open Sans", Arial, sans-serif;
    font-stretch: 75%;
  }
  .flyer {
    position: absolute; left: 300px; top: 55px;
    width: 600px; height: 850px;
    background: var(--paper);
    box-shadow: 0 4px 14px rgba(0,0,0,0.18);
    overflow: hidden;
  }
  /* Header */
  .header { position: absolute; left: 0; top: 0; width: 600px; height: 190px; padding: 38px 0 0 48px; }
  .brand { display: flex; align-items: center; gap: 14px; }
  .brand-mark { width: 26px; height: 26px; border-radius: 50%; background: var(--green); }
  .brand-name {
    color: var(--green); font-weight: 300; font-size: 58px;
    letter-spacing: 3px; text-transform: uppercase; line-height: 1;
  }
  .tagline {
    margin-top: 8px; color: var(--text-dark); font-weight: 400;
    font-size: 13px; letter-spacing: 2px; text-transform: uppercase;
  }
  .contact { margin-top: 12px; color: var(--green); font-size: 13px; font-weight: 400; line-height: 1.5; }

  /* Main photo */
  .photo-main {
    position: absolute; left: 0; top: 190px; width: 600px; height: 280px;
    background:
      radial-gradient(ellipse 160px 110px at 200px 150px, #f3e3a0 0%, #efe7c8 45%, rgba(230,230,230,0) 100%),
      radial-gradient(ellipse 140px 90px at 520px 40px, #f4b9b6 0%, #f4e28f 50%, rgba(240,240,240,0) 100%),
      linear-gradient(160deg, #eeeeee 0%, #c9c9cc 55%, #e6e6e8 100%);
  }
  .opening-badge {
    position: absolute; right: 0; top: 214px; width: 170px; height: 72px;
    background: var(--green); color: #fff; padding: 12px 0 0 18px;
  }
  .opening-badge .label { font-size: 16px; font-weight: 600; line-height: 1.1; }
  .opening-badge .date { font-size: 28px; font-weight: 600; line-height: 1.1; }

  /* Text band */
  .claims {
    position: absolute; left: 0; top: 470px; width: 600px; height: 140px;
    text-align: center; color: var(--text-grey); text-transform: uppercase;
    font-weight: 300; font-size: 19px; letter-spacing: 1.2px; line-height: 1.3;
    padding-top: 20px;
  }
  .claims .divider { display: block; margin: 8px auto 6px; }

  /* Bottom photos + coupon */
  .photo-products {
    position: absolute; left: 0; top: 610px; width: 510px; height: 240px;
    background:
      radial-gradient(ellipse 120px 100px at 120px 170px, #f2c1a6 0%, #f1e49a 45%, rgba(236,236,240,0) 100%),
      radial-gradient(ellipse 150px 90px at 380px 90px, #d8cde6 0%, #e9e1cf 55%, rgba(236,236,240,0) 100%),
      linear-gradient(180deg, #f0f0f3 0%, #dcdce2 100%);
  }
  .coupon {
    position: absolute; left: 510px; top: 610px; width: 90px; height: 240px;
    background: var(--green);
    border-left: 2px dashed var(--coupon-line);
  }
  .coupon-text {
    position: absolute; left: 50%; top: 50%;
    transform: translate(-50%, -50%) rotate(-90deg);
    white-space: nowrap; text-align: center; color: #fff; text-transform: uppercase;
  }
  .coupon-text .amount { font-size: 34px; font-weight: 400; letter-spacing: 1px; line-height: 1; }
  .coupon-text .scope { font-size: 14px; font-weight: 400; letter-spacing: 1px; margin-top: 4px; }
</style>
</head>
<body>
  <article class="flyer">
    <header class="header">
      <div class="brand">
        <span class="brand-name">Quorval Haus</span>
        <span class="brand-mark"></span>
      </div>
      <p class="tagline">Be natural with Quorval Haus</p>
      <p class="contact">
        info@quorvalhaus.de • www.quorvalhaus.de • Lindenweg 14 • 91234 Feldhausen<br>
        Öffnungszeiten: Freitags von 11:00 bis 18:00 Uhr
      </p>
    </header>

    <div class="photo-main" role="img" aria-label="Foto: handgerollte Badetrüffel mit Blütenblättern auf einem silbernen Teller, dahinter eine rosa-gelbe Blüte"></div>

    <div class="opening-badge">
      <div class="label">Neueröffnung am</div>
      <div class="date">05.05.2017</div>
    </div>

    <section class="claims">
      <p>Natürliche handgefertigte Naturseifen,</p>
      <p>Körper- und Gesichtspflegeprodukte und Dekorationsartikel.</p>
      <svg class="divider" width="60" height="12" viewBox="0 0 60 12" aria-hidden="true">
        <line x1="0" y1="6" x2="22" y2="6" stroke="#8cab2c" stroke-width="1.5"/>
        <circle cx="30" cy="6" r="4" fill="#8cab2c"/>
        <line x1="38" y1="6" x2="60" y2="6" stroke="#8cab2c" stroke-width="1.5"/>
      </svg>
      <p>Natürliche Inhaltsstoffe – 100% Paraben- und SLS-frei.</p>
    </section>

    <div class="photo-products" role="img" aria-label="Foto: Seifen- und Badecupcakes sowie lila marmorierte Naturseifenstücke"></div>

    <aside class="coupon">
      <div class="coupon-text">
        <div class="amount">20 % Rabatt</div>
        <div class="scope">Online &amp; im Laden</div>
      </div>
    </aside>
  </article>
</body>
</html>
```